Massage Therapy and Personal Training Business Card (Lorvex Wellness)

I need a logo design based in Washington. The company is called Lorvex Wellness. Lorvex are my initials. I specialize in massage therapy and personal training and general wellness of my clients. I've tried getting designs but haven't quite yet found what I'm looking for. I'm not inclined to a certain color yet but some color that resembles wellness such as light blue and white or green and white. Again, I'm not really picky about that. Thank you in advance

Industry/Entity Type

Business

Contact Information for Business Card

Have the description on one side and space for writing information on the back side such as number, appt, etc. I have an example attached. I see a lot of these card. I dont want the exact one, but something similar. Simple, professional and elegant.

Colors

Designer to choose colors to be used in the design.

Requirements
Must have
• Space on the back side to write
• A professional, elegant look
Should not have
• cartoon like style.

```html
<!DOCTYPE html>
<html lang="en">
<head>
<meta charset="utf-8">
<title>Lorvex Wellness – Business Card</title>
<link rel="stylesheet" href="https://fonts.googleapis.com/css2?family=Quicksand:wght@400;500;600&family=Open+Sans:wght@400;600&display=swap">
<style>
  :root {
    --backdrop: #cbcbcb;
    --card: #ffffff;
    --brand-blue: #0aa5e2;
    --brand-green: #6cbf3f;
    --muted: #8a8a8a;
    --rule: #bfe3f5;
    --anatomy-light: #f2f2f2;
    --anatomy-dark: #8e8e8e;
  }
  * { box-sizing: border-box; margin: 0; padding: 0; }
  html, body { width: 900px; height: 1200px; overflow: hidden; }
  body { background: var(--backdrop); position: relative; font-family: "Quicksand", sans-serif; }

  .card {
    position: absolute; left: 85px; width: 733px; height: 428px;
    background: var(--card); border-radius: 22px; overflow: hidden;
  }
  .card--front { top: 138px; }
  .card--back { top: 633px; }

  .front-art { position: absolute; inset: 0; }

  .brand { position: absolute; display: flex; align-items: center; gap: 10px; }
  .brand-name { font-family: "Quicksand", sans-serif; font-weight: 500; color: var(--brand-blue); white-space: nowrap; line-height: 1; }
  .brand-dot { border-radius: 50%; background: var(--brand-green); flex: none; }

  .card--front .brand { left: 290px; top: 78px; }
  .card--front .brand-name { font-size: 42px; }
  .card--front .brand-dot { width: 16px; height: 16px; }

  .tagline {
    position: absolute; left: 292px; top: 122px;
    font-family: "Open Sans", sans-serif; font-size: 12.5px; color: var(--muted); white-space: nowrap;
  }
  .tagline .sep { color: var(--brand-blue); }

  .person-name {
    position: absolute; right: 40px; top: 306px;
    font-size: 32px; font-weight: 400; color: #fff; white-space: nowrap;
  }
  .name-rule { position: absolute; left: 295px; right: 40px; top: 350px; height: 1.5px; background: #fff; }

  .contact { position: absolute; top: 360px; display: flex; align-items: center; gap: 7px;
    font-family: "Open Sans", sans-serif; font-size: 18px; color: #fff; white-space: nowrap; }
  .contact--email { left: 296px; }
  .contact--phone { right: 40px; }
  .contact-icon { width: 28px; height: 28px; flex: none; }

  .write-lines { position: absolute; left: 45px; right: 53px; top: 82px; }
  .write-line { height: 1px; background: var(--rule); margin-bottom: 61px; }

  .card--back .brand { right: 42px; bottom: 58px; }
  .card--back .brand-name { font-size: 30px; }
  .card--back .brand-dot { width: 12px; height: 12px; }
</style>
</head>
<body>

<section class="card card--front">
  <svg class="front-art" width="733" height="428" viewBox="0 0 733 428">
    <defs>
      <linearGradient id="anatomyTone" x1="0" y1="0" x2="1" y2="0">
        <stop offset="0" stop-color="var(--anatomy-dark)"/>
        <stop offset="0.5" stop-color="var(--anatomy-light)"/>
        <stop offset="1" stop-color="var(--anatomy-dark)"/>
      </linearGradient>
    </defs>
    <path class="wave-band" d="M 250 345 C 390 300, 560 245, 733 238 L 733 428 L 0 428 L 0 370 Z" fill="var(--brand-blue)"/>
    <path class="wave-stripe" d="M 360 285 C 480 232, 610 205, 715 207 C 610 216, 485 248, 372 290 Z" fill="var(--brand-blue)"/>
    <path class="wave-accent" d="M 195 318 C 255 290, 320 270, 378 262 C 322 282, 262 302, 200 324 Z" fill="var(--brand-green)"/>
    <rect class="anatomy-illustration" role="img" aria-label="Anatomical illustration of a muscular back with shoulders and elbows highlighted in blue"
          x="0" y="0" width="265" height="428" fill="url(#anatomyTone)"/>
  </svg>

  <div class="brand">
    <span class="brand-name">Lorvex Wellness</span>
    <span class="brand-dot"></span>
  </div>
  <p class="tagline">Massage therapy <span class="sep">•</span> Personal training <span class="sep">•</span> General wellness</p>

  <p class="person-name">Daniel Hayes</p>
  <div class="name-rule"></div>

  <p class="contact contact--email">info@lorvexwellness
    <svg class="contact-icon" viewBox="0 0 28 28" aria-hidden="true">
      <circle cx="14" cy="14" r="13" fill="var(--brand-green)" stroke="#fff" stroke-width="2"/>
      <rect x="7.5" y="9.5" width="13" height="9" rx="1" fill="#fff"/>
      <path d="M7.5 10 L14 15 L20.5 10" fill="none" stroke="var(--brand-green)" stroke-width="1.3"/>
    </svg>
  </p>
  <p class="contact contact--phone">801-555 0192
    <svg class="contact-icon" viewBox="0 0 28 28" aria-hidden="true">
      <circle cx="14" cy="14" r="13" fill="var(--brand-green)" stroke="#fff" stroke-width="2"/>
      <path d="M10 7.5 L12.5 10.5 L11 12.5 C12 14.5 13.5 16 15.5 17 L17.5 15.5 L20.5 18 L18.8 20.3 C13.5 20 8 14.5 7.7 9.2 Z" fill="#fff"/>
    </svg>
  </p>
</section>

<section class="card card--back">
  <div class="write-lines">
    <div class="write-line"></div>
    <div class="write-line"></div>
    <div class="write-line"></div>
    <div class="write-line"></div>
  </div>
  <div class="brand">
    <span class="brand-name">Lorvex Wellness</span>
    <span class="brand-dot"></span>
  </div>
</section>

</body>
</html>
```